Business Card Design

Alder Ridge Living Homes, Inc. (ARLH, Inc.) is a private, non-profit corporation which provides an array of services to individuals in a community setting. These services include residential, vocational/day, and therapeutic recreation that afford individuals the opportunity to integrate into the community and participate as valued members of society. We work with individuals with developmental disabilities, traumatic brain injury and the elderly. We are a very small company with approximately 100 employees. We have been in business since 1975. We are looking for a business card that is professional, trendy and little out of the box. The Executive Director likes colors that are in the blue or green family. Open to add other colors to the design. The business card needs to include a house. We currently have a design on our old webpage that he likes. The webpage is alderridgelivinghomes.org. He likes that a lot. There is also a picture on our Facebook page that someone drew that he likes. This will be the business card for our entire agency. All administrative staff in our agency will have the same business card but have their information plugged in.

Industry/Entity Type

Non-Profit

Contact Information for Business Card

For questions you will need to contact me, Margaret Tolliver at 555-814-3067 ext. 208. The information below will be used for the business card:

Gerald Whitcombe, Executive Director
Alder Ridge Living Homes, Inc.
418 W. Elm Avenue - PO Box 356
Fernwick, ST 27819
gerald.whitcombe@arlhinc.example
555-814-3067 - work
555-862-4093 - cell
555-814-5518 - fax

Requirements
Must have
• I am really open when it comes to design. The only design that must be included is a house

```html
<!DOCTYPE html>
<html lang="en">
<head>
<meta charset="utf-8">
<title>Alder Ridge Living Homes, Inc. — Business Card</title>
<link href="https://fonts.googleapis.com/css2?family=Caladea&family=Questrial&display=swap" rel="stylesheet">
<style>
  :root {
    --canvas: #ffffff;
    --green-edge: #5edc00;
    --green-mid: #7eff00;
    --ink: #1b1b1b;
    --band: #1c1c1c;
    --white: #ffffff;
    --accent: #e8191b;
  }
  * { margin: 0; padding: 0; box-sizing: border-box; }
  html, body { width: 1200px; height: 1000px; overflow: hidden; background: var(--canvas); }
  .canvas { position: relative; width: 1200px; height: 1000px; }

  .card {
    position: absolute; left: 308px; width: 583px; height: 332px;
    border-radius: 18px; overflow: hidden;
    background: linear-gradient(90deg, var(--green-edge) 0%, var(--green-mid) 45%, var(--green-mid) 60%, var(--green-edge) 100%);
  }
  .card--front { top: 116px; }
  .card--back { top: 556px; }

  .header-shape { position: absolute; left: 0; top: 0; }

  .company-name {
    position: absolute; left: 186px; top: 66px;
    font-family: "Caladea", serif; font-size: 24px; font-weight: 400; color: var(--white);
    white-space: nowrap;
  }
  .brand-square {
    position: absolute; left: 38px; top: 46px; width: 96px; height: 56px;
    background: var(--white); border-bottom: 4px solid var(--accent);
  }

  .person { position: absolute; left: 20px; top: 149px; font-family: "Caladea", serif; font-weight: 400; color: var(--ink); }
  .person__name { font-size: 22px; line-height: 26px; }
  .person__title, .person__email { font-size: 15px; line-height: 19px; }

  .contact { position: absolute; left: 406px; top: 150px; list-style: none;
    font-family: "Questrial", sans-serif; font-size: 14.5px; color: var(--ink); }
  .contact li { height: 22px; display: flex; align-items: center; gap: 9px; white-space: nowrap; }
  .contact svg { width: 14px; height: 14px; flex: none; }
  .contact .no-icon { padding-left: 23px; }

  .web-tab {
    position: absolute; left: 54px; bottom: 0; width: 476px; height: 27px;
    background: var(--band); border-radius: 14px 14px 0 0;
    display: flex; align-items: center; justify-content: center; gap: 12px;
    font-family: "Questrial", sans-serif; font-size: 17px; color: var(--white);
  }
  .web-tab svg { width: 15px; height: 15px; }

  .back-band {
    position: absolute; left: 0; top: 96px; width: 100%; height: 140px; background: var(--band);
    display: flex; align-items: center; justify-content: center; gap: 14px;
  }
  .back-band .brand-square { position: static; width: 70px; height: 70px; }
  .back-name { font-family: "Caladea", serif; font-size: 30px; font-weight: 400; line-height: 34px; color: var(--white); }
</style>
</head>
<body>
<main class="canvas">

  <section class="card card--front" aria-label="Business card front">
    <svg class="header-shape" width="583" height="123" viewBox="0 0 583 123" aria-hidden="true">
      <polygon points="0,0 94,0 135,41 583,41 583,122 0,122" fill="#1c1c1c"/>
    </svg>
    <div class="brand-square" aria-hidden="true"></div>
    <h1 class="company-name">Alder Ridge Living Homes, Inc.</h1>

    <div class="person">
      <p class="person__name">Gerald Whitcombe</p>
      <p class="person__title">Executive Director</p>
      <p class="person__email">gerald.whitcombe@arlhinc.example</p>
    </div>

    <ul class="contact">
      <li><svg viewBox="0 0 14 14"><path d="M7 1a4 4 0 0 0-4 4c0 3 4 8 4 8s4-5 4-8a4 4 0 0 0-4-4zm0 5.5A1.5 1.5 0 1 1 7 3.5a1.5 1.5 0 0 1 0 3z" fill="#1b1b1b"/></svg>418 W. Elm Avenue</li>
      <li><svg viewBox="0 0 14 14"><rect x="1" y="3" width="10" height="5" rx="2" fill="#1b1b1b"/><rect x="5" y="8" width="2" height="5" fill="#1b1b1b"/><rect x="9" y="1" width="1.5" height="4" fill="#1b1b1b"/></svg>356 Fernwick</li>
      <li class="no-icon">ST 27819</li>
      <li><svg viewBox="0 0 14 14"><path d="M3 1l2.5 3-1.5 1.5c.8 1.8 2 3 3.5 3.5L9 7.5l3 2.5-1.5 2.5C6 12 2 8 1.5 3z" fill="#1b1b1b"/></svg>555-814-3067</li>
      <li><svg viewBox="0 0 14 14"><rect x="3.5" y="0.5" width="7" height="13" rx="1" fill="none" stroke="#1b1b1b" stroke-width="1.4"/><circle cx="7" cy="11.3" r=".8" fill="#1b1b1b"/></svg>555-862-4093</li>
      <li><svg viewBox="0 0 14 14"><rect x="3" y="1" width="8" height="4" fill="#1b1b1b"/><rect x="1" y="5.5" width="12" height="5" fill="#1b1b1b"/><rect x="3" y="11" width="8" height="2" fill="#1b1b1b"/></svg>555-814-5518</li>
    </ul>

    <div class="web-tab">
      <svg viewBox="0 0 16 16"><circle cx="8" cy="8" r="7" fill="#ffffff"/><path d="M4 5l3 1 1 3-2 2 1 3M10 2l1 3 3 1" stroke="#1c1c1c" stroke-width="1.3" fill="none"/></svg>
      <span>www.arlhinc.example</span>
    </div>
  </section>

  <section class="card card--back" aria-label="Business card back">
    <div class="back-band">
      <div class="brand-square" aria-hidden="true"></div>
      <p class="back-name">Alder Ridge Living<br>Homes, Inc.</p>
    </div>
    <div class="web-tab">
      <svg viewBox="0 0 16 16"><circle cx="8" cy="8" r="7" fill="#ffffff"/><path d="M4 5l3 1 1 3-2 2 1 3M10 2l1 3 3 1" stroke="#1c1c1c" stroke-width="1.3" fill="none"/></svg>
      <span>www.arlhinc.example</span>
    </div>
  </section>

</main>
</body>
</html>
```